Paws and Meadows is a dog walking service that offers home boarding and pet taxi

I am looking for a eye catching A5 leaflet/flyer design for my dog walking business Paws and Meadows.

The flyer must have my company logo on it (jpeg), a picture of my van (jpeg) and a picture of dogs playing (jpegs 1-5).

The fonts must be easy to read. I am not set on any colour scheme but do like the idea of having a natural background. IE. Green grass and blue sky or some forest setting with green trees. If you don't like this idea or its hard to work with don't worry I am open minded so be creative and do what you thinks best.

I'll provide quick feedback to designs that i like and so we can work together.

The flyers must contain the following:

60 minute group and individual walks
GPS Tracked Walks
Home Boarding
Pet Taxi
Puppy/Pet visits

Offer: 50% off first weeks dogs walks with this flyer.

As well as containing my contact info:

07915382046
www.paws-and-meadows.co.uk
paws-and-meadows@mailbrook.co.uk

Chatterbook, Chirpline and Snapgallery logos must be present as well.

Thanks and Good luck!

Target Market(s)

ANYONE WHO NEEDS THEIR DOG WALKED OR LOOKED AFTER WHEN THEY ARE ON HOLIDAY

Industry/Entity Type

Business

Contact Information for Business Card

THE BUSINESS CARD MUST DISPLAY THE LOGO THAT HAS BEEN UPLOADED IN A FILE. IT MUST LOOK SHARP AND PROFESSIONAL. CONTAIN ALL CONTACT INFO AND HAVE SERVICES OFFERED. SEE PROJECT DESCRIPTION FOR FLYER.

Font styles to use
Serif
Sans Serif

Requirements
Must have
• SEE PROJECT DESCRIPTION
Nice to have
• IT WOULD BE NICE TO HAVE PHOTOS OF MY VAN AND DOGS PLAYING. I HAVE UPLOADED SOME PICS OF VAN TO BE USED AND THERE ARE PICS OF DOGS PLAYING THAT COULD BE USED.

```html
<!DOCTYPE html>
<html lang="en">
<head>
<meta charset="utf-8">
<title>Paws and Meadows – Dog Walking Flyer</title>
<link rel="stylesheet" href="https://fonts.googleapis.com/css2?family=Itim&display=swap">
<style>
  :root {
    --page: #000000;
    --ink: #111111;
    --white: #ffffff;
    --sky-top: #37b8ee;
    --sky-mid: #a9def6;
    --sky-low: #d6f0fa;
    --grass-light: #c9df3c;
    --grass-mid: #6cae2a;
    --grass-deep: #3f8a24;
    --ring: #f7a21b;
    --ring-soft: #ffe49a;
    --offer-top: #fde25a;
    --offer-bottom: #f59a1e;
    --photo-water: #6f7f8a;
    --photo-field: #5f9a3a;
    --van-body: #e9eef2;
    --chatter: #1f5fd6;
    --chirp: #1da6e8;
    --snap: #d9399a;
  }
  * { margin: 0; padding: 0; box-sizing: border-box; }
  html, body {
    width: 960px; height: 1200px; overflow: hidden;
    background: var(--page);
    font-family: "Itim", "Comic Sans MS", sans-serif;
  }
  .flyer {
    position: absolute; left: 146px; top: 116px;
    width: 671px; height: 952px; overflow: hidden;
  }
  .scene {
    position: absolute; inset: 0;
    background: linear-gradient(180deg,
      var(--sky-top) 0%, var(--sky-mid) 22%, var(--sky-low) 55%,
      #e6f3c0 62%, var(--grass-light) 68%, var(--grass-mid) 82%, var(--grass-deep) 100%);
  }
  .brand {
    position: absolute; left: 42px; top: 170px;
    display: flex; align-items: center; gap: 10px;
    font-size: 36px; color: var(--ink); letter-spacing: 0.5px;
  }
  .brand-dot {
    width: 22px; height: 22px; border-radius: 50%; background: var(--ring);
  }
  .headline {
    position: absolute; left: 340px; top: 76px; width: 320px;
    text-align: center; font-size: 35px; line-height: 42px;
    color: var(--ink); text-transform: uppercase; letter-spacing: 1px;
  }
  .services { position: absolute; left: 38px; top: 270px; list-style: none; }
  .services li {
    display: flex; align-items: center; height: 37.5px;
    font-size: 21px; color: var(--ink); letter-spacing: 0.4px;
  }
  .services svg { width: 26px; height: 24px; margin-right: 11px; fill: var(--ink); }
  .photo {
    position: absolute; border-radius: 50%;
    border: 5px solid var(--ring); box-shadow: 0 0 0 3px var(--ring-soft);
  }
  .photo-river { left: 464px; top: 180px; width: 180px; height: 180px;
    background: radial-gradient(circle at 60% 40%, #3a2c25 0 22%, transparent 23%), linear-gradient(180deg, #c9ccc9, var(--photo-water)); }
  .photo-stick { left: 432px; top: 326px; width: 156px; height: 156px;
    background: radial-gradient(circle at 35% 50%, #c89a5a 0 24%, transparent 25%), radial-gradient(circle at 65% 45%, #2a2523 0 24%, transparent 25%), var(--photo-field); }
  .photo-lawn { left: 20px; top: 493px; width: 134px; height: 134px;
    background: radial-gradient(circle at 50% 40%, #b8885a 0 18%, transparent 19%), var(--photo-field); }
  .van {
    position: absolute; left: 270px; top: 480px; width: 388px; height: 226px;
    border-radius: 40px 70px 30px 30px;
    background: linear-gradient(90deg, #3f8fd0 0%, #59a83a 55%, var(--van-body) 56%, var(--van-body) 100%);
    opacity: 0.95;
  }
  .offer {
    position: absolute; left: 139px; top: 528px; width: 160px; height: 160px;
    border-radius: 50%; border: 3px solid #fff2b8;
    background: linear-gradient(180deg, var(--offer-top), var(--offer-bottom));
    text-align: center; color: #2b2010; padding-top: 22px;
  }
  .offer-amount { font-size: 40px; line-height: 40px; }
  .offer-amount small { font-size: 14px; }
  .offer-terms { font-size: 17px; line-height: 21px; margin-top: 4px; }
  .contact {
    position: absolute; left: 18px; top: 830px; width: 310px;
    text-align: center; color: var(--white);
  }
  .contact-phone { font-size: 41px; line-height: 46px; letter-spacing: 1px; }
  .contact-web { font-size: 21px; line-height: 27px; }
  .contact-mail { font-size: 17.5px; line-height: 26px; }
  .social { position: absolute; left: 420px; top: 862px; color: var(--white); }
  .social-title { font-size: 19px; margin-bottom: 3px; }
  .social ul { list-style: none; }
  .social li { display: flex; align-items: center; gap: 7px; font-size: 15px; line-height: 20px; }
  .social span { width: 12px; height: 12px; border-radius: 50%; }
  .chatter { background: var(--chatter); }
  .chirp { background: var(--chirp); }
  .snap { background: var(--snap); }
</style>
</head>
<body>
<svg width="0" height="0" style="position:absolute">
  <symbol id="paw" viewBox="0 0 26 24">
    <ellipse cx="5" cy="9" rx="3" ry="3.6"/>
    <ellipse cx="10" cy="4" rx="3" ry="3.6"/>
    <ellipse cx="16" cy="4" rx="3" ry="3.6"/>
    <ellipse cx="21" cy="9" rx="3" ry="3.6"/>
    <path d="M13 11c-4 0-8 5-8 9 0 3 3 3 8 2 5 1 8 1 8-2 0-4-4-9-8-9z"/>
  </symbol>
</svg>

<main class="flyer">
  <div class="scene" role="img" aria-label="Background photo of blue sky over a green field with dogs running"></div>

  <div class="brand"><span class="brand-dot"></span>Paws and Meadows</div>

  <h1 class="headline">Caring for your<br>furry friend</h1>

  <ul class="services">
    <li><svg><use href="#paw"/></svg>60 minute group &amp; individual walks</li>
    <li><svg><use href="#paw"/></svg>GPS Tracked Walks</li>
    <li><svg><use href="#paw"/></svg>Home Boarding</li>
    <li><svg><use href="#paw"/></svg>Pet Taxi</li>
    <li><svg><use href="#paw"/></svg>Puppy/Pet visits</li>
  </ul>

  <div class="photo photo-river" role="img" aria-label="Photo of two dogs running through shallow water"></div>
  <div class="photo photo-stick" role="img" aria-label="Photo of two dogs carrying a stick together on grass"></div>
  <div class="van" role="img" aria-label="Photo of the branded company van parked on grass"></div>
  <div class="photo photo-lawn" role="img" aria-label="Photo of two dogs resting on a lawn"></div>

  <div class="offer">
    <div class="offer-amount">50% <small>off</small></div>
    <div class="offer-terms">first weeks<br>dogs walks with<br>this flyer.</div>
  </div>

  <div class="contact">
    <div class="contact-phone">07915382046</div>
    <div class="contact-web">www.paws-and-meadows.co.uk</div>
    <div class="contact-mail">paws-and-meadows@mailbrook.co.uk</div>
  </div>

  <div class="social">
    <div class="social-title">Follow us on</div>
    <ul>
      <li><span class="chatter"></span>Chatterbook</li>
      <li><span class="chirp"></span>Chirpline</li>
      <li><span class="snap"></span>Snapgallery</li>
    </ul>
  </div>
</main>
</body>
</html>
```